International Property Consultancy

Brief Overview:

I need a dynamic and well designed website that is easy to use and understand. It has to be unique and different to generic templates that most websites seem to be these days. PLEASE NO GENERIC TEMPLATES FROM THE INTERNET.

Our business has 10 years experience working on struggling international developments that we then work in-house for to turn around and brings bout success. We stay within a project often for long periods of time until success is achieved. We are unique in our approach and completely different to the standard routes to market for many developments. The site is for developers to see what we have done in regards to previous projects, as such we want to incorporate video into this site with a strong design aesthetic. There will be videos of the past projects we have worked on, which will act as case studies.

I like very simple but punchy websites, that people can navigate and understand very easily. Also a big fan of unique and well thought out design aesthetic.

Initial Site layout thoughts:

1) Homepage:
2) About Us
3) What we've done / Work
This part has the projects we have worked on (France, Portugal, London, Morocco). Each one will have some video content and photo images, but also would be good to have a succinct way to mention what we did and the successes in a clever and punchy way.

4) Contact Us

* This is just a guideline. Would be open to input and creative direction on your own part.

*More details and websites we like can be seen in the brief doc attached.

PLEASE VIEW THE WIREFRAME WORD DOC ATTACHED.

Here there are also some more examples to help:

Here are just a few examples of websites and what I like about them:

- www.velmoro.com (clean, nice geometric design aesthetic, good animation when loading and changing pages well thought out all though also coulee be considered a bit dull and basic after the initial homepage slide)
- https://www.farbridgehub.net (Clean site, quite clinical, lacks video content and doesn't engage greatly).
- https://ruskotile.com (minimal, and like how it mixes the design aesthetic more with video and photo content)

- https://www.amberquillworks.com (like the layout of this and how it displays the projects and work section)

- https://brisk.com (Good use of video content)

- https://loomfield.studio (minimal to the point and mixes design with video and animation etc...)

Here is another couple of cool websites that may help give you some direction: https://halvenquay.com www.brisk.com

Hi there, One of the things I thought would be good on the homepage is to add the logo with a 'digital landscape' before flicking down into a slide with video content of the projects... Just an idea but have posted some pics in the brief. We would get this animated for the site. But if you have better ideas, please do run with them. Thanks,

Target Market(s)

Property developers

Number of Pages Required

4 page

Font styles to use
Other font styles liked:
• Read brief

Requirements
Must have
• Needs to be clean, dynamic and easy to follow on desktop and mobile. We will use it as a kind of portfolio website so will need to embed video of past projects we have worked on.

Read brief in docs.
Nice to have
• Clean
Should not have
• Not be another generic template website.
Not have random property stock photos. (We are not a property agency).

```html
<!DOCTYPE html>
<html lang="en">
<head>
<meta charset="utf-8">
<title>olvanti. — International Property Consultancy</title>
<link rel="stylesheet" href="https://fonts.googleapis.com/css2?family=Montserrat:wght@400;500;600;700;800&display=swap">
<style>
  :root {
    --white: #ffffff;
    --ink: #1a1a1a;
    --body-text: #333333;
    --footer-bg: #2b2b2b;
    --band-black: #050505;
    --teal-button: #2c5763;
    --panel-white: rgba(255,255,255,0.93);
    --overlay-dark: rgba(20,24,30,0.35);
  }
  * { box-sizing: border-box; margin: 0; padding: 0; }
  html, body { width: 1200px; height: 3600px; overflow: hidden; }
  body { font-family: "Montserrat", sans-serif; color: var(--white); background: var(--footer-bg); position: relative; }

  .section { position: absolute; left: 0; width: 1200px; overflow: hidden; }
  .photo { position: absolute; inset: 0; }

  /* Header */
  .site-header { position: absolute; top: 0; left: 0; width: 1200px; height: 68px; z-index: 5; background: rgba(40,40,40,0.35); }
  .site-header .brand { position: absolute; left: 200px; top: 14px; font-size: 28px; font-weight: 600; letter-spacing: 0.5px; }
  .menu-toggle { position: absolute; left: 958px; top: 22px; width: 44px; height: 26px; }
  .menu-toggle span { display: block; height: 4px; background: var(--white); margin-bottom: 7px; border-radius: 1px; }

  /* Hero */
  .hero { top: 0; height: 771px; }
  .hero .photo { background: linear-gradient(180deg, #6c7580 0%, #b8a37e 22%, #a7794a 40%, #4a4a4f 65%, #2c2f36 100%); }
  .hero-logo { position: absolute; left: 0; width: 1200px; top: 318px; text-align: center; font-size: 118px; font-weight: 600; letter-spacing: 1px; line-height: 1; }

  .scroll-cue { position: absolute; left: 0; width: 1200px; text-align: center; font-size: 16px; font-weight: 700; }
  .scroll-cue svg { display: block; margin: 2px auto 0; }

  /* About */
  .about { top: 771px; height: 771px; }
  .about .photo { background: linear-gradient(180deg, #6d7883 0%, #5e6b76 40%, #3d4a54 70%, #2a333b 100%); }
  .about-lead { position: absolute; top: 170px; left: 0; width: 1200px; text-align: center; font-size: 31px; font-weight: 600; line-height: 42px; }
  .about-card { position: absolute; left: 472px; top: 300px; width: 728px; height: 299px; background: var(--panel-white); color: var(--ink); padding: 14px 16px; }
  .about-card h2 { font-size: 34px; font-weight: 600; margin-bottom: 10px; }
  .about-card p { width: 505px; font-size: 12.3px; line-height: 15.4px; color: var(--body-text); margin-bottom: 15px; }

  /* Projects banner */
  .projects-banner { top: 1542px; height: 428px; }
  .projects-banner .photo { background: linear-gradient(180deg, #8a9aa6 0%, #5b4a3c 35%, #3d2e24 65%, #2f4a58 85%, #223844 100%); }
  .projects-banner h2 { position: absolute; top: 172px; left: 0; width: 1200px; text-align: center; font-size: 64px; font-weight: 700; }

  /* Project grid */
  .project-tile { position: absolute; width: 600px; height: 386px; overflow: hidden; }
  .project-tile h3 { position: absolute; top: 148px; left: 0; width: 600px; text-align: center; font-size: 42px; font-weight: 700; letter-spacing: 1px; }
  .view-button { position: absolute; top: 208px; left: 240px; width: 120px; height: 25px; border-radius: 13px; background: var(--teal-button); font-size: 11px; font-weight: 700; text-align: center; line-height: 25px; }
  .tile-france { left: 0; top: 1970px; }
  .tile-france .photo { background: linear-gradient(180deg, #7f93a8 0%, #b9b3a1 45%, #8f7a52 75%, #3f4a2e 100%); }
  .tile-morocco { left: 600px; top: 1970px; }
  .tile-morocco .photo { background: linear-gradient(180deg, #4b6278 0%, #5f6f80 45%, #8a6b58 75%, #3b3f48 100%); }
  .tile-london { left: 0; top: 2355px; }
  .tile-london .photo { background: linear-gradient(180deg, #6e8aa6 0%, #9cb0c2 40%, #5a4a3a 75%, #2f2f33 100%); }
  .tile-portugal { left: 600px; top: 2355px; }
  .tile-portugal .photo { background: linear-gradient(180deg, #5a86b8 0%, #a9b9c8 35%, #9d8466 65%, #4d5d66 100%); }

  .load-band { top: 2741px; height: 87px; background: var(--band-black); }
  .load-more { position: absolute; left: 507px; top: 24px; width: 188px; height: 38px; border: 2px solid var(--white); border-radius: 12px; font-size: 15px; font-weight: 700; text-align: center; line-height: 34px; }
  .load-more svg { vertical-align: -2px; margin-left: 4px; }

  /* Contact */
  .contact { top: 2828px; height: 514px; }
  .contact .photo { background: linear-gradient(110deg, #3d4048 0%, #6b6a70 35%, #8d7f78 60%, #a48f84 100%); }
  .contact-card { position: absolute; left: 0; top: 257px; width: 659px; height: 257px; background: var(--panel-white); color: var(--ink); padding: 80px 0 0 197px; }
  .contact-card h2 { font-size: 34px; font-weight: 600; margin-bottom: 8px; }
  .contact-list { list-style: none; font-size: 13px; color: var(--body-text); }
  .contact-list li { height: 19.5px; display: flex; align-items: center; gap: 8px; }

  /* Footer */
  .site-footer { top: 3342px; height: 258px; background: var(--footer-bg); }
  .footer-brand { position: absolute; top: 62px; left: 0; width: 1200px; text-align: center; font-size: 42px; font-weight: 600; }
  .social-links { position: absolute; top: 136px; left: 0; width: 1200px; display: flex; justify-content: center; gap: 22px; font-size: 13px; font-weight: 600; }
  .social-links span { display: flex; align-items: center; gap: 6px; }
  .social-links i { display: inline-block; width: 10px; height: 10px; border-radius: 50%; background: var(--white); }
  .footer-rule { position: absolute; top: 214px; left: 0; width: 1200px; height: 1px; background: rgba(255,255,255,0.45); }
  .footer-nav { position: absolute; top: 226px; left: 197px; display: flex; gap: 18px; font-size: 13px; }
  .copyright { position: absolute; top: 224px; left: 847px; font-size: 13px; }
</style>
</head>
<body>

<header class="site-header">
  <div class="brand">olvanti.</div>
  <div class="menu-toggle" aria-label="Menu"><span></span><span></span><span></span></div>
</header>

<section class="section hero">
  <div class="photo" role="img" aria-label="City skyline of high-rise towers at sunset"></div>
  <div class="hero-logo">olvanti.</div>
  <div class="scroll-cue" style="top:705px">About Us
    <svg width="14" height="16" viewBox="0 0 14 16"><path d="M2 2l5 5 5-5M2 9l5 5 5-5" fill="none" stroke="#fff" stroke-width="2.4"/></svg>
  </div>
</section>

<section class="section about">
  <div class="photo" role="img" aria-label="Downtown skyline with a tall observation tower at dusk"></div>
  <p class="about-lead">We Specialise in the fulfilment of<br>international property developments</p>
  <div class="about-card">
    <h2>About Us</h2>
    <p>Olvanti is a consultancy company that helps international property developments fulfil their potential. The company has had great success over the last 10 years of turning around struggling property developments (often resort and investment) and making them reach their maximum potential. We have completed projects in Portugal, London, France, Morocco, Brazil etc...</p>
    <p>We work by white labelling or working in-house for each project creating a strategy that is bespoke and unique for each project. It allows a project to purely gain from any initiatives, i.e.. unlike paying agents to promote your project and gain from marketing spend etc.</p>
  </div>
  <div class="scroll-cue" style="top:715px">Projects
    <svg width="14" height="16" viewBox="0 0 14 16"><path d="M2 2l5 5 5-5M2 9l5 5 5-5" fill="none" stroke="#fff" stroke-width="2.4"/></svg>
  </div>
</section>

<section class="section projects-banner">
  <div class="photo" role="img" aria-label="Timber lodge resort beside a pool at dusk"></div>
  <h2>Projects</h2>
</section>

<article class="project-tile tile-france">
  <div class="photo" role="img" aria-label="Paris tower under a cloudy sky"></div>
  <h3>France</h3><div class="view-button">View Now</div>
</article>
<article class="project-tile tile-morocco">
  <div class="photo" role="img" aria-label="Seaside mosque with tall minaret at dusk"></div>
  <h3>Morocco</h3><div class="view-button">View Now</div>
</article>
<article class="project-tile tile-london">
  <div class="photo" role="img" aria-label="Westminster clock tower and parliament by the river"></div>
  <h3>London</h3><div class="view-button">View Now</div>
</article>
<article class="project-tile tile-portugal">
  <div class="photo" role="img" aria-label="Colourful riverside old town of Porto"></div>
  <h3>Portugal</h3><div class="view-button" style="left:225px">View Now</div>
</article>

<section class="section load-band">
  <div class="load-more">Load More
    <svg width="12" height="12" viewBox="0 0 12 12"><path d="M10 6a4 4 0 1 1-1.2-2.9M9 1v2.5H6.5" fill="none" stroke="#fff" stroke-width="1.5"/></svg>
  </div>
</section>

<section class="section contact">
  <div class="photo" role="img" aria-label="Two hands passing a pen over a contract document"></div>
  <div class="contact-card">
    <h2>Contact Us</h2>
    <ul class="contact-list">
      <li><svg width="10" height="11" viewBox="0 0 10 11"><path d="M5 10S1.5 6.5 1.5 4a3.5 3.5 0 0 1 7 0C8.5 6.5 5 10 5 10z" fill="none" stroke="#333" stroke-width="1"/><circle cx="5" cy="4" r="1.2" fill="#333"/></svg>Harlow Lane 412, London</li>
      <li><svg width="10" height="11" viewBox="0 0 10 11"><path d="M2 1h2l1 2.5-1.3 1a6 6 0 0 0 2.8 2.8l1-1.3L10 7v2a1 1 0 0 1-1 1A8 8 0 0 1 1 2a1 1 0 0 1 1-1z" fill="none" stroke="#333" stroke-width="1"/></svg>80412937015</li>
      <li><svg width="11" height="9" viewBox="0 0 11 9"><rect x="0.5" y="0.5" width="10" height="8" fill="none" stroke="#333"/><path d="M0.5 0.5l5 4.5 5-4.5" fill="none" stroke="#333"/></svg>hello@olvanti-mail.com</li>
      <li><svg width="10" height="10" viewBox="0 0 10 10"><circle cx="5" cy="5" r="4.5" fill="#333"/><path d="M0.5 5h9M5 0.5c2 2.5 2 6.5 0 9M5 0.5c-2 2.5-2 6.5 0 9" fill="none" stroke="#fff" stroke-width="0.7"/></svg>www.olvanti.com</li>
    </ul>
  </div>
</section>

<footer class="section site-footer">
  <div class="footer-brand">olvanti.</div>
  <div class="social-links">
    <span><i></i>Linkloop</span>
    <span><i></i>Snapframe</span>
    <span><i></i>Streamly</span>
  </div>
  <div class="footer-rule"></div>
  <nav class="footer-nav"><span>Home</span><span>About Us</span><span>Projects</span><span>Contact Us</span></nav>
  <div class="copyright">Copyright olvanti 2020</div>
</footer>

</body>
</html>
```